Lena Corvell Business Card

I need a business card that reflects my current website: itslenacorvell.example and screenshot attached. If we keep the color scheme of the site and sample card below that would be ideal. The business card should include the information on the attached sample cards.

Industry/Entity Type

Business

```html
<!DOCTYPE html>
<html lang="en">
<head>
<meta charset="utf-8">
<title>Lena Corvell Business Card</title>
<link rel="stylesheet" href="https://fonts.googleapis.com/css2?family=Open+Sans:wght@400&family=PT+Sans+Narrow:wght@400&display=swap">
<style>
  :root {
    --page-bg: #efece8;
    --card-teal: #68c4b2;
    --card-grey: #c9c9c9;
    --ink-white: #ffffff;
    --chalk: #f4f4f4;
    --photo-light: #d2d2d2;
    --photo-warm: #8a5a3c;
    --photo-denim: #7c9cc0;
  }
  * { box-sizing: border-box; margin: 0; padding: 0; }
  html, body {
    width: 1200px; height: 1200px; overflow: hidden;
    background: var(--page-bg);
  }
  .canvas { position: relative; width: 1200px; height: 1200px; }

  .card {
    position: absolute;
    box-shadow: 0 6px 18px rgba(0,0,0,0.18);
    overflow: hidden;
  }

  /* Front */
  .card-front {
    left: 80px; top: 90px; width: 756px; height: 466px;
    background: var(--card-teal);
    color: var(--ink-white);
  }
  .front-name {
    position: absolute; right: 36px; top: 110px;
    font-family: "PT Sans Narrow", sans-serif;
    font-size: 64px; line-height: 1;
    letter-spacing: 1px;
  }
  .front-name .prefix { font-size: 36px; margin-right: 10px; }
  .tagline {
    position: absolute; right: 38px; top: 184px;
    font-family: "PT Sans Narrow", sans-serif;
    font-size: 20px; white-space: nowrap;
  }
  .tagline .sep { margin: 0 10px; }
  .contact-list {
    position: absolute; right: 36px;
    list-style: none;
    font-family: "Open Sans", sans-serif;
    font-size: 16px; line-height: 22.5px;
    text-align: right;
  }
  .contact-direct { top: 270px; }
  .contact-social { top: 363px; }
  .contact-list li { display: flex; justify-content: flex-end; align-items: center; gap: 8px; white-space: nowrap; }
  .contact-icon { width: 20px; height: 20px; flex: none; }

  /* Back */
  .card-back {
    left: 305px; top: 578px; width: 760px; height: 475px;
    background: var(--card-grey);
  }
  .back-photo {
    position: absolute; inset: 0;
    background: radial-gradient(ellipse 190px 240px at 600px 260px, var(--photo-warm) 0%, var(--photo-denim) 55%, rgba(124,156,192,0) 75%),
                linear-gradient(180deg, var(--photo-light), var(--card-grey));
  }
  .back-name {
    position: absolute; left: 30px; top: 220px;
    font-family: "PT Sans Narrow", sans-serif;
    font-size: 64px; line-height: 1;
    color: var(--chalk);
    letter-spacing: 1px;
  }
  .back-name .prefix { font-size: 36px; margin-right: 10px; }
</style>
</head>
<body>
<main class="canvas">

  <section class="card card-front" aria-label="Card front">
    <h1 class="front-name"><span class="prefix">its</span>Lena Corvell</h1>
    <p class="tagline">Brand Curator<span class="sep">|</span>Digital Storyteller<span class="sep">|</span>Social Entrprenuer</p>

    <ul class="contact-list contact-direct">
      <li>555.014.2290
        <svg class="contact-icon" viewBox="0 0 20 20" aria-hidden="true"><circle cx="10" cy="10" r="8.8" fill="none" stroke="#fff" stroke-width="1.4"/><path d="M5.5 9.5c0-2 2-3 4.5-3s4.5 1 4.5 3l-2 .4-.4-1.6h-4.2l-.4 1.6z M7 11h6v3H7z" fill="#fff"/></svg>
      </li>
      <li>me@lenacorvell.example
        <svg class="contact-icon" viewBox="0 0 20 20" aria-hidden="true"><circle cx="10" cy="10" r="8.8" fill="none" stroke="#fff" stroke-width="1.4"/><rect x="5" y="6.5" width="10" height="7" fill="none" stroke="#fff" stroke-width="1.3"/><path d="M5 6.5l5 4 5-4" fill="none" stroke="#fff" stroke-width="1.3"/></svg>
      </li>
      <li>www.itslenacorvell.example
        <svg class="contact-icon" viewBox="0 0 20 20" aria-hidden="true"><circle cx="10" cy="10" r="8.8" fill="none" stroke="#fff" stroke-width="1.4"/><circle cx="10" cy="10" r="5" fill="none" stroke="#fff" stroke-width="1.1"/><ellipse cx="10" cy="10" rx="2.2" ry="5" fill="none" stroke="#fff" stroke-width="1"/><path d="M5 10h10" stroke="#fff" stroke-width="1"/></svg>
      </li>
    </ul>

    <ul class="contact-list contact-social">
      <li>www.friendbook.example/ItsLenaCorvell
        <svg class="contact-icon" viewBox="0 0 20 20" aria-hidden="true"><circle cx="10" cy="10" r="8.8" fill="none" stroke="#fff" stroke-width="1.4"/></svg>
      </li>
      <li>www.chirper.example/ItsLenaCorvell
        <svg class="contact-icon" viewBox="0 0 20 20" aria-hidden="true"><circle cx="10" cy="10" r="8.8" fill="none" stroke="#fff" stroke-width="1.4"/></svg>
      </li>
      <li>www.snapgrid.example/itslenacorvell
        <svg class="contact-icon" viewBox="0 0 20 20" aria-hidden="true"><circle cx="10" cy="10" r="8.8" fill="none" stroke="#fff" stroke-width="1.4"/></svg>
      </li>
    </ul>
  </section>

  <section class="card card-back" aria-label="Card back">
    <div class="back-photo" role="img" aria-label="Portrait photo of Lena Corvell in a denim jacket, smiling and holding chalk against a grey chalkboard wall"></div>
    <p class="back-name"><span class="prefix">its</span>Lena Corvell</p>
  </section>

</main>
</body>
</html>
```